Logo needed for business card

Velquist Pty Ltd is in the business of healthcare and ecommerce.

We own and manage pharmacies and online health ecomerce sites.

We provide ecommerce consultants for companies looking for an ecommerce business startegy.

Think of it as the umbrella under which several healthcare brands may sit.

When I think of Velquist, I visulaise slick black/metalic colours, so please stay away from the common blue and green colours that seem to be so popular in this field.

Target Market(s)

CEOs and COOs

Industry/Entity Type

Healthcare

Contact Information for Business Card

Tessa Lindqvist
Director
Velquist Pty Ltd
4/362 Fennick Pde
Brellton, NSW 2148

Requirements
Must have
• Design must have scope to be implemented on the company's website and letterheads etc.

```html
<!DOCTYPE html>
<html lang="en">
<head>
<meta charset="utf-8">
<title>Velquist Pty Ltd – Business Card</title>
<link rel="stylesheet" href="https://fonts.googleapis.com/css2?family=Cinzel:wght@400&family=Ubuntu:wght@400&display=swap">
<style>
  :root {
    --backdrop: #3c3c3c;
    --card-black: #161616;
    --card-edge: #1f1f1f;
    --text-white: #f2f2f2;
    --text-soft: #d8d8d8;
    --accent-red: #d3202a;
    --panel-grey: #555555;
    --panel-line: #666666;
  }
  html, body {
    margin: 0;
    padding: 0;
    width: 1200px;
    height: 949px;
    overflow: hidden;
    background: var(--backdrop);
  }
  .canvas {
    position: relative;
    width: 1200px;
    height: 949px;
  }
  .business-card {
    position: absolute;
    left: 150px;
    top: 217px;
    width: 900px;
    height: 515px;
    background: linear-gradient(180deg, var(--card-edge) 0%, var(--card-black) 100%);
    overflow: hidden;
  }
  .brand {
    position: absolute;
    left: 0;
    right: 0;
    top: 190px;
    display: flex;
    justify-content: center;
    align-items: center;
    gap: 16px;
  }
  .brand-mark {
    width: 16px;
    height: 16px;
    background: var(--accent-red);
  }
  .brand-name {
    margin: 0;
    font-family: "Cinzel", serif;
    font-weight: 400;
    font-size: 42px;
    letter-spacing: 1px;
    color: var(--text-white);
  }
  .address {
    position: absolute;
    left: 0;
    right: 0;
    top: 252px;
    margin: 0;
    text-align: center;
    font-family: "Ubuntu", sans-serif;
    font-size: 19px;
    color: var(--text-soft);
  }
  .contact-panel {
    position: absolute;
    left: 256px;
    top: 376px;
    width: 410px;
    height: 134px;
    background: var(--panel-grey);
    border-top: 1px solid var(--panel-line);
    display: flex;
    flex-direction: column;
    justify-content: center;
    align-items: center;
    font-family: "Ubuntu", sans-serif;
  }
  .person-name {
    margin: 0;
    font-size: 31px;
    color: var(--text-white);
    line-height: 1.2;
  }
  .person-role {
    margin: 0;
    font-size: 28px;
    color: var(--accent-red);
    line-height: 1.2;
  }
</style>
</head>
<body>
  <main class="canvas">
    <section class="business-card" aria-label="Business card">
      <div class="brand">
        <span class="brand-mark" aria-hidden="true"></span>
        <h1 class="brand-name">Velquist Pty Ltd</h1>
      </div>
      <p class="address">4/362 Fennick Pde Brellton, NSW 2148</p>
      <div class="contact-panel">
        <p class="person-name">Tessa Lindqvist</p>
        <p class="person-role">Director</p>
      </div>
    </section>
  </main>
</body>
</html>
```